The Lune Fox Organic & Natural Soaps needs a good business card

I am sorry for the lack of direction or Scope of the project. I am new at this board.
This is my scope and requirements:
Business card project:
This is related to the Label project I also opened up. (The Lune Fox Organic & Natural Soaps is looking for label designs (along with the business card project (Contest) )
I have attached an initial draft at a logo I tried to come up with for a business card and labelling/marketing. I am hoping that you can take this logo and 'run with it' to finesse it, make it look unique and professional. I am open to new logo ideas.
I am a start up at home company making Organic and Natural Bar soaps, hand soaps, body washes.
All of my ingredients are organic or natural and will include natural essential oils, exfoliants, natural powders/colours, etc.
Some of the names are: Brambelle (feisty, energetic soap), Dunes (more of a sandalwood earthy tones with a sandalwood powder exfoliant), Frost (maybe changing this name - fresh scented), Plum Cedar (lemongrass/ginger, exfoliants), etc....
I am attaching the cardstock I am looking at for packaging as well - this might help with the business card aspect. I was originally just looking at plain kraft paper but am receiving samples of Vera Pindle coloured kraft paper. I may still print business cards on the plain kraft though.. not sure.
If you need more information, please let me know.
Moira
Business Card and Labels
I have come up with a basic logo that I like. If you can finesse it and provide a great business card, that would be great.
I am starting up an at home soap business that will include luxury organic bar soaps, luxury natural olive oil bar soaps, organic hand wash, natural olive oil based body wash. I will be selling online and at shows.
please find attached my logo idea that I would like to incorporate.
I am also looking at packaging/labelling ideas for the bar soaps (prefer kraft cardstock wrap) and labels for the various body washes (natural soap) and the hand washes (organic). The hand washes will be in 250ml square bottles and the body wash will be in tapered bottles (smaller at top going to bottom).
Please let me know if you need more info!
I am also looking for packaging (label design for hand soap/body wash bottles and label design for organic/natural soaps)
This Project coincides with the business card project I also posted: there are 2 projects related - 1) business cards, 2) labels for organic hand wash, natural body wash, sticker label or design for kraft paper to package around luxury organic and natural soaps. I am not sure if a sticker would look nice or the design for the thick kraft paper.
Thank you!
Business card project:
This is related to the Label project I also opened up. (The Lune Fox Organic & Natural Soaps is looking for label designs (along with the business card proje (Contest) )
I have attached an initial draft at a logo I tried to come up with for a business card and labelling/marketing. I am hoping that you can take this logo and 'run with it' to finesse it, make it look unique and professional.
Moira
Hello; I just wanted to let everyone know that if you feel that this
brand needs a different logo, I am open to ideas (if you don't think the
one I started with is ok). I am coming to the experts here!
Just to confirm also - this is related to the label/packaging project, therefore, there are 2 projects, 2 payments! :)
Cheers

```html
<!DOCTYPE html>
<html lang="en">
<head>
<meta charset="utf-8">
<title>The Lune Fox Organic &amp; Natural Soaps – Business Card</title>
<link rel="stylesheet" href="https://fonts.googleapis.com/css2?family=Oleo+Script:wght@700&family=Alfa+Slab+One&display=swap">
<style>
  :root {
    --kraft: #b39a72;
    --kraft-light: #bda47b;
    --kraft-band: #c3ad82;
    --forest: #3a4324;
    --ink: #2b271c;
    --cream: #f1e8cc;
    --dots: #4a3e2a;
  }
  * { margin: 0; padding: 0; box-sizing: border-box; }
  html, body { width: 733px; height: 1200px; overflow: hidden; background: var(--kraft); }
  .card {
    position: relative;
    width: 733px;
    height: 1200px;
    overflow: hidden;
    background: radial-gradient(ellipse at 50% 40%, var(--kraft-light), var(--kraft) 75%);
    font-family: "Alfa Slab One", Georgia, serif;
    color: var(--ink);
  }
  .brand-name {
    position: absolute;
    left: 0; top: 250px; width: 733px;
    text-align: center;
    font-family: "Alfa Slab One", Georgia, serif;
    font-size: 72px;
    line-height: 1;
    color: var(--forest);
  }
  .connectors { position: absolute; left: 0; top: 0; }
  .holder-name {
    position: absolute; left: 0; width: 733px; top: 600px;
    text-align: center;
    font-family: "Oleo Script", cursive; font-weight: 700;
    font-size: 54px; line-height: 1.2; color: var(--ink); padding-left: 10px;
  }
  .holder-role {
    position: absolute; left: 288px; top: 682px; width: 160px; height: 48px;
    border: 3px solid var(--ink);
    display: flex; align-items: center; justify-content: center;
    font-size: 26px;
  }
  .company-pill {
    position: absolute; left: 56px; top: 876px; width: 616px; height: 62px;
    background: var(--forest); border-radius: 26px;
    display: flex; align-items: center; justify-content: center;
    color: var(--cream); font-size: 27px; letter-spacing: -0.2px;
  }
  .contact {
    position: absolute; left: 0; width: 733px; text-align: center;
    font-size: 29px; color: var(--ink);
  }
  .contact--phone { top: 966px; padding-right: 100px; display: flex; justify-content: center; align-items: center; gap: 12px; }
  .contact--email { top: 1030px; font-size: 28px; }
  .phone-icon { width: 30px; height: 30px; }
  .footer-block { position: absolute; left: 0; top: 1120px; width: 56px; height: 80px; background: var(--forest); }
  .footer-band {
    position: absolute; left: 83px; top: 1120px; width: 650px; height: 80px;
    background: var(--kraft-band);
    display: flex; align-items: center; justify-content: flex-start;
    padding-left: 122px; font-size: 28px;
  }
</style>
</head>
<body>
<main class="card">
  <p class="brand-name">The Lune Fox</p>

  <svg class="connectors" width="733" height="1200" aria-hidden="true">
    <g fill="none" stroke="var(--dots)" stroke-width="4" stroke-dasharray="2 6" stroke-linecap="round">
      <polyline points="212,640 125,640 125,703 286,703"/>
      <polyline points="450,703 589,703 589,863"/>
    </g>
  </svg>

  <h1 class="holder-name">Moira Hollis</h1>
  <div class="holder-role">Owner</div>

  <div class="company-pill">The Lune Fox Organic &amp; Natural Soaps</div>

  <p class="contact contact--phone">
    <svg class="phone-icon" viewBox="0 0 30 30" aria-hidden="true">
      <circle cx="15" cy="15" r="13" fill="none" stroke="var(--ink)" stroke-width="2.5"/>
      <path d="M11 8 h3 l1 4 -2 1.5 c1 2.5 2.5 4 5 5 l1.5 -2 4 1 v3 c-7 1 -13.5 -5.5 -12.5 -12.5z" fill="var(--ink)"/>
    </svg>
    <span>(416) 555-0142</span>
  </p>
  <p class="contact contact--email">Moira@thelunefox.ca</p>

  <div class="footer-block"></div>
  <div class="footer-band">www.thelunefox.ca</div>
</main>
</body>
</html>
```